Typing Service Business Card Design

Need a new business card design for new logo update. The Keyline Crew is an outsourced typing service. We type audio / voice files into word documents. We are a professional service that is recognised in the industry over the past 15 years and have a strong connection to our brand. The final design should be professional, simple, yet effective.

Business

Contact Information for Business Card

Rosalind Varga
Director

rosalind@kbq.com.au
www.thekeylinecrewbase.com.au

```html
<!DOCTYPE html>
<html lang="en">
<head>
<meta charset="utf-8">
<title>The Keyline Crew – Business Card</title>
<link rel="stylesheet" href="https://fonts.googleapis.com/css2?family=Lato:wght@400;700;900&display=swap">
<style>
  :root {
    --ink: #1c1b1c;
    --magenta: #c63d8a;
    --paper: #f1f1f1;
    --white: #ffffff;
    --muted: #b9b9b9;
    --rule: #3a393a;
    --stage: #e6e6e8;
  }
  * { box-sizing: border-box; margin: 0; padding: 0; }
  html, body { width: 1200px; height: 800px; overflow: hidden; }
  body {
    background: var(--stage);
    position: relative;
    font-family: "Lato", sans-serif;
  }
  .card {
    position: absolute;
    width: 520px;
    height: 300px;
    top: 250px;
    overflow: hidden;
    background: var(--ink);
    box-shadow: 0 10px 28px rgba(0,0,0,0.18);
  }
  .card-front { left: 50px; }
  .card-back { left: 630px; }
  .card-art { position: absolute; inset: 0; width: 100%; height: 100%; }

  .brand-name {
    font-family: "Lato", sans-serif;
    font-weight: 700;
    white-space: nowrap;
  }

  /* Front */
  .front-brand {
    position: absolute;
    left: 180px;
    width: 330px;
    top: 138px;
    text-align: center;
  }
  .front-brand .brand-name { color: var(--white); font-size: 34px; line-height: 1.2; }
  .front-rule {
    position: absolute;
    left: 205px; top: 218px;
    width: 260px; height: 1px;
    background: var(--rule);
  }

  /* Back */
  .back-brand {
    position: absolute;
    left: 44px; width: 210px;
    top: 136px;
    text-align: center;
  }
  .back-brand .brand-name { color: var(--ink); font-size: 20px; line-height: 1.2; }

  .contact {
    position: absolute;
    left: 268px; top: 82px;
    color: var(--white);
  }
  .contact-name { font-size: 16px; letter-spacing: 0.3px; text-transform: uppercase; }
  .contact-name .first { font-weight: 900; }
  .contact-name .last { font-weight: 400; }
  .contact-role { font-size: 10px; color: var(--muted); text-transform: uppercase; margin-top: 1px; }
  .contact-list { list-style: none; margin-top: 24px; }
  .contact-item {
    display: flex; align-items: center; gap: 10px;
    font-size: 10.5px; margin-bottom: 17px;
  }
  .contact-icon {
    width: 22px; height: 22px;
    background: var(--magenta);
    border-radius: 3px;
    display: flex; align-items: center; justify-content: center;
    flex: none;
  }
</style>
</head>
<body>

  <section class="card card-front" aria-label="Business card front">
    <svg class="card-art" viewBox="0 0 520 300" preserveAspectRatio="none" aria-hidden="true">
      <polygon points="0,0 285,300 70,300 0,224" fill="var(--magenta)"/>
    </svg>
    <div class="front-brand">
      <p class="brand-name">The Keyline Crew</p>
    </div>
    <div class="front-rule"></div>
  </section>

  <section class="card card-back" aria-label="Business card back">
    <svg class="card-art" viewBox="0 0 520 300" preserveAspectRatio="none" aria-hidden="true">
      <rect x="0" y="0" width="44" height="300" fill="var(--magenta)"/>
      <polygon points="0,0 18,0 44,30 44,32 0,0" fill="var(--ink)"/>
      <polygon points="0,205 44,255 44,300 0,300" fill="var(--ink)"/>
      <rect x="44" y="0" width="210" height="300" fill="var(--paper)"/>
      <polygon points="440,0 520,0 520,80" fill="var(--magenta)"/>
      <polygon points="254,255 254,300 290,300" fill="var(--magenta)"/>
    </svg>

    <div class="back-brand">
      <p class="brand-name">The Keyline Crew</p>
    </div>

    <div class="contact">
      <p class="contact-name"><span class="first">Rosalind</span> <span class="last">Varga</span></p>
      <p class="contact-role">Director</p>
      <ul class="contact-list">
        <li class="contact-item">
          <span class="contact-icon">
            <svg width="13" height="10" viewBox="0 0 13 10" aria-hidden="true">
              <rect x="0.6" y="0.6" width="11.8" height="8.8" fill="none" stroke="#fff" stroke-width="1.2"/>
              <polyline points="0.8,0.8 6.5,5.5 12.2,0.8" fill="none" stroke="#fff" stroke-width="1.2"/>
            </svg>
          </span>
          <span>rosalind@kbq.com.au</span>
        </li>
        <li class="contact-item">
          <span class="contact-icon">
            <svg width="13" height="13" viewBox="0 0 13 13" aria-hidden="true">
              <circle cx="6.5" cy="6.5" r="5.6" fill="none" stroke="#fff" stroke-width="1.2"/>
              <ellipse cx="6.5" cy="6.5" rx="2.4" ry="5.6" fill="none" stroke="#fff" stroke-width="1"/>
              <line x1="0.9" y1="6.5" x2="12.1" y2="6.5" stroke="#fff" stroke-width="1"/>
            </svg>
          </span>
          <span>www.thekeylinecrewbase.com.au</span>
        </li>
      </ul>
    </div>
  </section>

</body>
</html>
```